Business Card Design

My focus is upon the over 75s, for whom I designed a specialised massage technique (I am qualified as a naturopath). The title is a play on the Japanese words for 'red', and for 'person' (I'm ethnically Australian, but am from Japan), and mirrors the Japanese word for 'baby' (miss/master red). There should be plenty of red used in the card, and, if possible, reflect vitality, vigour, vibrancy, without being garish, harsh, or too bright.

Target Market(s)

All ages, but specifically the over 75s.

Industry/Entity Type

Massage

Contact Information for Business Card

Tolu-ve
Mobile Massage
0487206143
Relax, Deep Tissue, Facials
Custom-Designed Massage for the over 75s
Locals and Seniors (75+) Discounts

```html
<!DOCTYPE html>
<html lang="en">
<head>
<meta charset="utf-8">
<title>Tolu-ve Mobile Massage — Business Card</title>
<link rel="stylesheet" href="https://fonts.googleapis.com/css2?family=Mulish:wght@400;800&display=swap">
<style>
  :root {
    --canvas: #e9e9ea;
    --card-body: #242021;
    --card-edge: #3a3536;
    --screen: #ffffff;
    --bubble-red-deep: #a8232c;
    --bubble-red: #c93a3c;
    --bubble-red-light: #e0675a;
    --bubble-rose: #f2d9d6;
    --ink: #2a1a1b;
    --ink-light: #ffffff;
    --button: #ffffff;
  }
  * { box-sizing: border-box; margin: 0; padding: 0; }
  html, body {
    width: 1200px; height: 634px; overflow: hidden;
    background: var(--canvas);
    font-family: "Mulish", "Century Gothic", sans-serif;
  }
  .card {
    position: absolute; left: 100px; top: 37px;
    width: 1000px; height: 560px;
    border-radius: 44px;
    background: var(--card-body);
    box-shadow: inset 0 0 0 3px var(--card-edge);
  }
  .card__screen {
    position: absolute; left: 60px; top: 30px;
    width: 700px; height: 500px;
    background: var(--screen);
    overflow: hidden;
  }
  .card__home-button {
    position: absolute; left: 838px; top: 235px;
    width: 90px; height: 90px; border-radius: 50%;
    background: var(--button);
  }
  .bubble {
    position: absolute;
    width: 168px;
    border-radius: 30px;
  }
  .bubble__text {
    position: absolute; inset: 0;
    padding: 26px 24px;
    writing-mode: vertical-rl;
    transform: rotate(180deg);
    font-size: 21px; line-height: 1.25;
    white-space: nowrap;
  }
  .bubble__text span { display: block; }
  .bubble--sent {
    background: linear-gradient(90deg, var(--bubble-red-deep), var(--bubble-red) 50%, var(--bubble-red-light));
    color: var(--ink-light);
  }
  .bubble--sent::after {
    content: ""; position: absolute; right: -26px; top: 0;
    border-top: 24px solid var(--bubble-red-light);
    border-right: 30px solid transparent;
  }
  .bubble--received {
    background: var(--bubble-rose);
    color: var(--ink);
  }
  .bubble--received::after {
    content: ""; position: absolute; left: -26px; bottom: 0;
    border-bottom: 24px solid var(--bubble-rose);
    border-left: 30px solid transparent;
  }
  .bubble--intro   { left: 52px;  top: 26px;  height: 330px; }
  .bubble--services{ left: 266px; top: 112px; height: 336px; }
  .bubble--contact { left: 480px; top: 150px; height: 320px; }
  .bubble__name { font-weight: 800; }
</style>
</head>
<body>
  <div class="card">
    <div class="card__screen">
      <div class="bubble bubble--sent bubble--intro">
        <div class="bubble__text">
          <span class="bubble__name">Tolu-ve Mobile Massage</span>
          <span>0487206143 Relax,</span>
          <span>Deep Tissue,</span>
        </div>
      </div>
      <div class="bubble bubble--received bubble--services">
        <div class="bubble__text">
          <span>Facials Custom</span>
          <span>Designed Massage</span>
          <span>over 75s Locals and Seniors</span>
          <span>(75+) Discounts</span>
        </div>
      </div>
      <div class="bubble bubble--sent bubble--contact">
        <div class="bubble__text">
          <span>www.Your web address</span>
          <span>email@example.com</span>
        </div>
      </div>
    </div>
    <div class="card__home-button"></div>
  </div>
</body>
</html>
```